Book Cover for a book on Quiet Ledgers

I am self-publishing my book on Bookvale and need a book cover made. Below are the details. See attached templates for size we need to use. I also attached a previous cover we had made that I liked. The problem with it was they were two boys helping each other but the book is about women. I'm open to your ideas on the cover though, but I wanted to show you a style I liked as an idea.
Front of Cover
Book Title: Quiet Ledgers
Book Subtitle: Morning Letters of a Harbor Keeper
Author Name: Lorna T. Beckett
Add on the Spine of Cover: Quiet Ledgers and Lorna T. Beckett
Back of the Cover Text:
Quiet Ledgers: Morning Letters of a Harbor Keeper is an honest account of a business owner’s experience attempting to navigate the start-up community while also pursuing spiritual growth. Author Lorna Beckett defines a spiritual entrepreneur as “someone who runs an enterprise with the purpose of growing love rather than material gain.” This book discusses the three dimensions of Quiet Ledgers:
1. The business is an integral part of the founder’s spiritual journey.
2. Employees working for the spiritual enterprise, whether they know it or not, encounter this company because it's part of their spiritual path.
3. The business itself has a life force of its own and its purpose is to further the kingdom of heaven on earth.
These three dimensions happen simultaneously and work together to produce the greatest possible result. However, this can feel confusing to a founder juggling these dimensions while also trying to manage and run a business. This is not a formulaic self-help book or roadmap. Rather, it is a compilation of personal reflections that often seem at odds with the traditional world of entrepreneurship.
Below the description add my picture (see attached for my picture)
Bio text:
Lorna Beckett founded Tellway with the vision of ushering in a life-long education system that shifts away from standardization to one that empowers people to live their purpose. In college, Lorna interned for Bright Lanterns, a women’s empowerment initiative where she recognized her passion for helping people find their voice. Lorna's 20-year journey has come full circle to empowering other female CEOs who are pursuing the path of Quiet Ledgers.
NOTE: Please note that Bookvale puts a bar code on the bottom right of the back cover as is noted on the attached template.
Size template is attached to the brief, here are the sizes typed out:
# Description Width (in) Height (in)
1 Full Cover 12.79 9.25
2 Front Cover 6 9
3 Safe Area 5.875 8.75
4 Bleed 0.125 0.125
5 Margin 0.125 0.125
6 Spine 0.54 9
7 Spine Safe Area 0.415 8.75
8 Spine Margin 0.062 0.062
9 Barcode Margin 0.25 0.25
Pre-publication checklist
BOOKVALE TIPS for the final cover:
1. Save as a PDF. Your cover must be a single PDF that includes the back cover, spine, and front cover as one image.
2. Flatten all transparencies. These can cause the file to print with missing or distorted content. Consult your software's documentation to learn how.
3. Embed your fonts. Consult your software's documentation to learn how.
4. Remove crop marks, color bars, template text. Crop marks are lines showing where pages should be trimmed. Color bars are strips with a series of patches used to ensure color balance during printing. Also, remove any template text, PDF creation guides, or software references.
5. Ensure your cover image meets the minimum resolution of 300 DPI (dots per inch).
6. Optimize PDFs. Optimization is useful to reduce your file size, allowing for higher performance when transferring, uploading, viewing, and printing the files.
7. Remove file security. Locked or encrypted files will fail review.
Target Market(s)
Women who want to be CEOs or are currently CEOs of companies.
Industry/Entity Type
Entrepreneurship, business, spirituality
Requirements
Must have
- Just the text on the description. A very welcoming feel.
Nice to have
- I like the idea of having a sunrise/sunset in the image somehow like in the example I attached to the brief, but again I'm open.
Should not have
- Please don't put any yoga or meditation poses or hands outstretched. I have a lot of interesting ones that look like my example so if you are going to submit after Saturday 10/29, please only do so if you have a new idea! Thanks!

```html
<!DOCTYPE html>
<html lang="en">
<head>
<meta charset="utf-8">
<title>Quiet Ledgers — Book Cover</title>
<link rel="stylesheet" href="https://fonts.googleapis.com/css2?family=Noto+Serif+Display:wght@400;500&display=swap">
<style>
  :root {
    --ink: #000000;
    --title-gold: #f7d300;
    --subtitle-ink: #1c1c1c;
    --author-white: #ffffff;
    --sky-top: #7db7bf;
    --sky-mid: #d9dc93;
    --sun-glow: #fbe26a;
    --horizon: #e0a92a;
    --ridge: #3b2e1d;
  }
  html, body {
    margin: 0;
    padding: 0;
    width: 800px;
    height: 1200px;
    overflow: hidden;
    background: var(--ink);
  }
  .cover {
    position: relative;
    width: 800px;
    height: 1200px;
    background: var(--ink);
    font-family: "Noto Serif Display", Georgia, serif;
    overflow: hidden;
  }
  .cover-art {
    position: absolute;
    top: 0;
    left: 0;
    width: 800px;
    height: 660px;
    display: block;
  }
  .subtitle {
    position: absolute;
    top: 70px;
    left: 0;
    width: 800px;
    margin: 0;
    text-align: center;
    font-size: 28px;
    font-weight: 400;
    letter-spacing: 2.5px;
    text-transform: uppercase;
    color: var(--subtitle-ink);
  }
  .title {
    position: absolute;
    top: 718px;
    left: 0;
    width: 800px;
    margin: 0;
    text-align: center;
    color: var(--title-gold);
    font-weight: 400;
    text-transform: uppercase;
    line-height: 1;
  }
  .title-main {
    display: block;
    font-size: 116px;
    letter-spacing: 4px;
  }
  .title-second {
    display: block;
    margin-top: 10px;
    font-size: 64px;
    letter-spacing: 3px;
  }
  .author {
    position: absolute;
    top: 1084px;
    left: 0;
    width: 800px;
    margin: 0;
    text-align: center;
    font-size: 48px;
    font-weight: 400;
    letter-spacing: 1px;
    color: var(--author-white);
  }
</style>
</head>
<body>
  <main class="cover">
    <svg class="cover-art" viewBox="0 0 800 660" role="img" aria-label="Photograph of a sunrise over a sea of golden clouds seen from a dark rocky summit, fading into black at the bottom">
      <defs>
        <linearGradient id="sky" x1="0" y1="0" x2="0" y2="1">
          <stop offset="0" stop-color="var(--sky-top)"/>
          <stop offset="0.35" stop-color="var(--sky-mid)"/>
          <stop offset="0.55" stop-color="var(--sun-glow)"/>
          <stop offset="0.72" stop-color="var(--horizon)"/>
          <stop offset="0.85" stop-color="var(--ridge)"/>
          <stop offset="1" stop-color="var(--ink)"/>
        </linearGradient>
        <radialGradient id="sun" cx="0.6" cy="0.62" r="0.45">
          <stop offset="0" stop-color="#fff6c0" stop-opacity="0.9"/>
          <stop offset="0.4" stop-color="#fbe26a" stop-opacity="0.5"/>
          <stop offset="1" stop-color="#fbe26a" stop-opacity="0"/>
        </radialGradient>
      </defs>
      <rect width="800" height="660" fill="url(#sky)"/>
      <rect width="800" height="660" fill="url(#sun)"/>
    </svg>

    <p class="subtitle">Morning Letters of a Harbor Keeper</p>

    <h1 class="title">
      <span class="title-main">Quiet</span>
      <span class="title-second">Ledgers</span>
    </h1>

    <p class="author">Lorna T. Beckett</p>
  </main>
</body>
</html>
```